Mark Dunvale actor business cards

I need unique and interesting business cards that have my headshot photo, my name, tagline/position/skills, contact info, preferred pronouns (he, him, his), and social media handles. These need to be memorable networking tools to hand out at events that stand out. I am an actor that works in theatre, film, and TV and usually play darker dramatic roles, though it doesn't have to necessarily need to be reflected in the design, but I am not a light, comedic actor. In my email tagline, My position/skills are "Actor, storyteller, theatre maker."

Target Market(s)

Casting directors, film and television community, theatre community.

Industry/Entity Type

Performing Art

Contact Information for Business Card

Mark Dunvale. Pronouns: he, him, his. Contact info: (555)-318-7406, Markdunvale.example, markdunvale@mailbox.example. Talent representation: Corvanti Talent Agency. Social Media: Friendbook page, chirpit and snapgram: @MarkDunvaleActs. Company Member of Larkhollow Theatre Company.

Font styles to use
Serif
Decorative

Colors

Designer to choose colors to be used in the design.

Requirements
Must have
• Headshot photo, name, tagline, preferred pronouns, contact info, Social media handle, talent agency logo, larkhollow theatre company logo. Both logos should be smaller than my name. Under or near Larkhollow logo, it should say "Company Member"
Nice to have
• I would like to have the photo, my name, tagline, and maybe pronouns on one side, and all contact info, and social media, and talent agency logo on the other. I would like the style to reflect my type which is a little more serious and somewhat darker, and definitely not comedic.
Should not have
• No extraneous theatre lights, camera, or film, etc. clip art or photos. Use solid backgrounds or photos provided.

```html
<!DOCTYPE html>
<html lang="en">
<head>
<meta charset="utf-8">
<title>Mark Dunvale – Business Cards</title>
<link href="https://fonts.googleapis.com/css2?family=Cormorant+Garamond:ital,wght@0,500;1,500;1,600&family=Lato:wght@400&display=swap" rel="stylesheet">
<style>
  :root {
    --stage: #303030;
    --paper: #ffffff;
    --ink: #111111;
    --lavender: #7c80b6;
    --lavender-text: #e4e5f3;
    --teal: #1490b1;
    --night: #000000;
    --photo-top: #d9d4cf;
    --photo-bottom: #4f5f96;
  }
  * { box-sizing: border-box; margin: 0; padding: 0; }
  html, body { width: 1200px; height: 900px; overflow: hidden; }
  body { background: var(--stage); position: relative; font-family: "Lato", Arial, sans-serif; }

  .card { position: absolute; top: 275px; width: 477px; height: 293px; overflow: hidden; }
  .card--front { left: 116px; background: var(--paper); border-radius: 0 44px 0 44px; }
  .card--back { left: 622px; background: var(--teal); border-radius: 44px 0 44px 0; }

  .agency-mark { position: absolute; display: flex; flex-direction: column; align-items: flex-end; line-height: 1; }
  .agency-mark__name { font-family: "Cormorant Garamond", Georgia, serif; font-weight: 500; font-size: 44px; letter-spacing: 0.5px; }
  .agency-mark__sub { font-family: "Cormorant Garamond", Georgia, serif; font-weight: 500; font-size: 12px; margin-top: 2px; }
  .card--front .agency-mark { left: 22px; top: 64px; color: var(--ink); }
  .card--back .agency-mark { left: 26px; top: 74px; color: var(--paper); }

  .headshot { position: absolute; right: 0; top: 0; width: 212px; height: 293px;
    background: linear-gradient(180deg, var(--photo-top) 0%, #b9a9a0 38%, var(--photo-bottom) 72%, #3f4d80 100%); }

  .person-name { position: absolute; left: 22px; top: 166px; font-family: "Cormorant Garamond", Georgia, serif;
    font-style: italic; font-weight: 600; font-size: 25px; color: var(--ink); letter-spacing: 0.6px; }
  .person-role { position: absolute; left: 23px; top: 195px; font-size: 13.5px; color: var(--ink); }

  .pronoun-band { position: absolute; left: 0; top: 233px; width: 266px; height: 60px; background: var(--lavender); }
  .pronoun-band__text { position: absolute; left: 22px; top: 12px; font-family: "Cormorant Garamond", Georgia, serif;
    font-style: italic; font-weight: 500; font-size: 27px; color: var(--lavender-text); letter-spacing: 0.5px; }

  .night-panel { position: absolute; left: 0; top: 0; width: 477px; height: 293px; }

  .contact-list { position: absolute; left: 25px; top: 210px; list-style: none; color: var(--paper); font-size: 13.5px; line-height: 17px; }
  .contact-list li { display: flex; align-items: center; gap: 4px; }
  .contact-list svg { width: 10px; height: 10px; fill: var(--paper); }

  .social { position: absolute; right: 36px; top: 221px; display: flex; flex-direction: column; align-items: flex-end; color: var(--paper); }
  .social__dots { display: flex; gap: 4px; margin-bottom: 3px; margin-right: 1px; }
  .social__dots span { width: 17px; height: 17px; border-radius: 50%; background: var(--paper); }
  .social__handle { font-size: 13.5px; }
</style>
</head>
<body>

<section class="card card--front" aria-label="Card front">
  <div class="agency-mark">
    <span class="agency-mark__name">Corvanti</span>
    <span class="agency-mark__sub">Talent Agency</span>
  </div>
  <h1 class="person-name">Mark Dunvale</h1>
  <p class="person-role">Actor, Storyteller, Theatre Maker</p>
  <div class="pronoun-band"><span class="pronoun-band__text">He, Him, His</span></div>
  <div class="headshot" role="img" aria-label="Headshot photo of Mark Dunvale in a blue shirt"></div>
</section>

<section class="card card--back" aria-label="Card back">
  <svg class="night-panel" viewBox="0 0 477 293" aria-hidden="true">
    <path d="M398 0 H477 V293 H250 C300 250 330 200 345 140 C355 90 370 40 398 0 Z" fill="var(--night)"/>
  </svg>
  <div class="agency-mark">
    <span class="agency-mark__name">Corvanti</span>
    <span class="agency-mark__sub">Talent Agency</span>
  </div>
  <ul class="contact-list">
    <li><svg viewBox="0 0 10 10"><path d="M1 3 Q5 0 9 3 L8 5 L6.5 4 V3.5 H3.5 V4 L2 5 Z M2.5 5.5 H7.5 L8.5 9 H1.5 Z"/></svg>555-318-7406</li>
    <li><svg viewBox="0 0 10 10"><path d="M0.5 2 H9.5 V8.5 H0.5 Z" /><path d="M0.8 2.3 L5 5.5 L9.2 2.3" stroke="var(--teal)" stroke-width="1" fill="none"/></svg>markdunvale@mailbox.example</li>
    <li><svg viewBox="0 0 10 10"><circle cx="5" cy="5" r="4.6"/><path d="M0.6 5 H9.4 M5 0.6 C2.5 3 2.5 7 5 9.4 M5 0.6 C7.5 3 7.5 7 5 9.4" stroke="var(--teal)" stroke-width="0.8" fill="none"/></svg>www.Markdunvale.example</li>
  </ul>
  <div class="social">
    <div class="social__dots" aria-hidden="true"><span></span><span></span><span></span></div>
    <span class="social__handle">@MarkDunvaleActs</span>
  </div>
</section>

</body>
</html>
```